Dining hall menu app needs a redesign

We are looking for a redesign of our app TrayPlate which is available for iOS for free on the Kestrel AppHub.

The app allows students of most of Germany's universities to show the menu of their university's dining hall. Currently there are about 400 dining halls to view the menu of. A menu contains the a list of meals for the next couple of days (usually for the next 5-7 days). Each meal can be rated by the users and photos can be uploaded. The following data should be visible for each meal in the meal list:
- The date the meal is available
- The meal category (usually a short text, categorizing the meal)
- Name of the meal (can be very long but it's ok to truncate it after the second line)
- Average meal rating (5-star rating)
- A photo of the meal
- Up to 4 prices (e.g. usually students pay less than employees, which is why multiple prices for the same meal are available. In the menu list only the prices are shown)

When selecting a meal, more details about the meal are shown:
- Full meal name
- Up to 4 prices including the price type (e.g. Student: 3.40€, Employees: 4.20€)
- Total number of ratings
- Total number of comments
- A list of additives and info-texts about the meal (e.g. whether the meal is vegetarian, or contains food additives)
- A list of photos including a relative date when the photo has been taken (e.g. "2 months ago")

Additionally a user should be able to add a review to the meal (5 star rating and an optional comment), view the list of comments, take a photo of the meal and to share it on chatterbook/blipster/via email.

All views show an advertisement banner on the bottom of the view.

The design should be very modern and clean. We don't like a skeuomorphic design. The content of the app is most important. Other than that you are free to design something pretty.
Updates

Target Market(s)

Students (age between 19 and 30)

Industry/Entity Type

University

Requirements
Must have
• At least we need a redesign of the meal list, the meal detail page, the app-logo and the splashscreen.
Nice to have
• Design for the meal review page, the dining hall list and the favorites list.
Should not have
• No skeuomorphic design and not too many colors.

```html
<!DOCTYPE html>
<html lang="en">
<head>
<meta charset="utf-8">
<title>TrayPlate – meal info and canteen list</title>
<link rel="stylesheet" href="https://fonts.googleapis.com/css2?family=Arimo:wght@400;700&family=Satisfy&display=swap">
<style>
:root{
  --backdrop:#141619;
  --screen:#22282f;
  --bar:#1b1f24;
  --nav:#252b32;
  --divider:#15191d;
  --row:#3a4652;
  --row-dark:#2b333c;
  --section:#2a3139;
  --list:#2a3038;
  --accent:#e9452f;
  --text:#dde2e7;
  --muted:#9aa3ad;
  --star:#f2b21b;
  --star-off:#2a3139;
  --icon:#8fa0b0;
}
*{box-sizing:border-box;margin:0;padding:0}
html,body{width:1200px;height:849px;overflow:hidden;background:var(--backdrop)}
body{font-family:"Arimo",Arial,sans-serif;color:var(--text)}
.stage{position:relative;width:1169px;height:827px;transform:scale(1.0265);transform-origin:0 0}
.screen{position:absolute;top:70px;width:467px;height:702px;background:var(--screen);overflow:hidden}
.screen--info{left:66px}
.screen--list{left:635px}
.status{height:30px;background:var(--bar);display:flex;align-items:center;padding:0 8px;font-weight:700;font-size:18px;color:#fff;position:relative}
.status .signal{display:flex;align-items:flex-end;gap:2px;margin-right:4px;height:12px}
.status .signal i{display:block;width:3px;background:#fff}
.status .carrier{margin-right:12px}
.status .lock{position:absolute;left:50%;top:6px;transform:translateX(-50%)}
.status .battery{position:absolute;right:8px;top:9px}
.navbar{height:63px;background:var(--nav);display:flex;align-items:center;position:relative;border-bottom:4px solid var(--accent)}
.navbar .title{position:absolute;left:0;right:0;text-align:center;font-family:"Satisfy",cursive;font-size:36px;color:#fff;pointer-events:none}
.nav-btn{width:68px;height:63px;display:flex;align-items:center;justify-content:center;border-right:1px solid var(--divider)}
.nav-btn.right{border-right:none;border-left:1px solid var(--divider)}
.spacer{flex:1}
.gallery{height:203px;background:var(--screen);position:relative;border-bottom:3px solid var(--accent)}
.photo{position:absolute;top:10px;height:184px;border:2px solid #e8e8e8;border-radius:5px;overflow:hidden}
.photo .date{position:absolute;top:8px;left:0;right:0;text-align:center;color:#fff;font-size:17px;text-shadow:0 1px 2px rgba(0,0,0,.7)}
.photo--a{left:-8px;width:188px;background:linear-gradient(160deg,#b44a2a,#d89a5c 55%,#7a3a22)}
.photo--b{left:190px;width:207px;background:linear-gradient(170deg,#3d5163,#e0c26a 50%,#6a4420)}
.photo--c{left:405px;width:80px;background:linear-gradient(160deg,#6a7a3a,#c8a25a 55%,#8a3a2a)}
.ratings{height:39px;background:var(--row-dark);display:flex;align-items:center;justify-content:space-between;padding:0 10px;font-weight:700;font-size:18px;color:var(--muted)}
.stars{display:flex;gap:1px}
.desc{padding:5px 10px 0;font-size:18px;line-height:30px;height:93px;color:var(--text)}
.row{display:flex;align-items:center;justify-content:space-between;padding:0 14px;background:var(--row);font-weight:700;font-size:18px;border-top:1px solid var(--divider)}
.row .price{color:var(--accent);font-weight:400}
.row--price{height:45px}
.row--header{height:38px;background:var(--section);color:var(--text)}
.rate-box{height:61px;background:var(--row);display:flex;align-items:center;justify-content:center;gap:4px;border-top:1px solid var(--divider)}
.row--link{height:48px}
.row--header.last{height:30px;align-items:flex-start;padding-top:6px}
.venue{height:119px;border-bottom:1px solid var(--divider);background:var(--list);position:relative;padding:10px 14px}
.venue h2{font-size:24px;font-weight:700;color:var(--text)}
.venue .distance{margin-top:12px;font-size:19px;font-weight:700;color:var(--muted);display:flex;align-items:center;gap:5px}
.venue .address{margin-top:6px;font-size:19px;color:var(--accent)}
.fav{position:absolute;right:15px;top:27px;width:60px;height:59px;background:#20252b;border-radius:3px;display:flex;align-items:center;justify-content:center}
.tabbar{position:absolute;left:0;right:0;bottom:0;height:67px;background:var(--bar);display:flex}
.tab{flex:1;display:flex;flex-direction:column;align-items:center;justify-content:flex-end;padding-bottom:4px;font-size:16px;color:#7f8892;border-left:1px solid #2c3239;gap:4px}
.tab:first-child{border-left:none;background:#20252b;color:#fff}
</style>
</head>
<body>
<svg width="0" height="0" style="position:absolute">
  <defs>
    <symbol id="star" viewBox="0 0 24 24"><path d="M12 1.5l3.1 6.8 7.4.8-5.5 5 1.6 7.3L12 17.7l-6.6 3.7 1.6-7.3-5.5-5 7.4-.8z"/></symbol>
    <symbol id="heart" viewBox="0 0 24 24"><path d="M12 21s-9-6.2-9-12.2C3 5.6 5.3 3.5 8 3.5c1.8 0 3.2 1 4 2.3.8-1.3 2.2-2.3 4-2.3 2.7 0 5 2.1 5 5.3C21 14.8 12 21 12 21z"/></symbol>
    <symbol id="pin" viewBox="0 0 24 24"><path d="M12 1C7.6 1 4.5 4.2 4.5 8.4 4.5 14 12 23 12 23s7.5-9 7.5-14.6C19.5 4.2 16.4 1 12 1zm0 10.5a3 3 0 110-6 3 3 0 010 6z"/></symbol>
  </defs>
</svg>

<div class="stage">
  <!-- Meal detail screen -->
  <section class="screen screen--info">
    <div class="status">
      <span class="signal"><i style="height:3px"></i><i style="height:5px"></i><i style="height:7px"></i><i style="height:9px"></i><i style="height:12px"></i></span>
      <span class="carrier">NIMBUS</span><span>3G</span>
      <svg class="lock" width="14" height="17" viewBox="0 0 14 17"><path d="M3 7V5a4 4 0 018 0v2" fill="none" stroke="#fff" stroke-width="2"/><rect x="1" y="7" width="12" height="10" rx="1" fill="#fff"/></svg>
      <svg class="battery" width="28" height="13" viewBox="0 0 28 13"><rect x="1" y="1" width="23" height="11" rx="2" fill="none" stroke="#fff" stroke-width="1.5"/><rect x="3" y="3" width="19" height="7" fill="#fff"/><rect x="25" y="4" width="2.5" height="5" fill="#fff"/></svg>
    </div>
    <header class="navbar">
      <div class="nav-btn"><svg width="40" height="40" viewBox="0 0 40 40"><circle cx="20" cy="20" r="18" fill="none" stroke="var(--icon)" stroke-width="2"/><path d="M29 20H12m7-7l-7 7 7 7" fill="none" stroke="var(--icon)" stroke-width="2.5" stroke-linecap="round" stroke-linejoin="round"/></svg></div>
      <span class="title">info</span>
      <div class="spacer"></div>
      <div class="nav-btn right"><svg width="40" height="40" viewBox="0 0 40 40"><circle cx="20" cy="20" r="18" fill="none" stroke="var(--icon)" stroke-width="2"/><path d="M13 27c1-6 5-9 11-9v-4l6 6-6 6v-4c-4 0-8 1-11 5z" fill="var(--icon)"/></svg></div>
      <div class="nav-btn right"><svg width="40" height="40" viewBox="0 0 40 40"><circle cx="20" cy="20" r="18" fill="none" stroke="var(--icon)" stroke-width="2"/><path d="M11 15h4l2-3h6l2 3h4v12H11z" fill="var(--icon)"/><circle cx="20" cy="21" r="4" fill="var(--nav)"/></svg></div>
    </header>
    <div class="gallery">
      <div class="photo photo--a" role="img" aria-label="Photo of a plate of spaghetti with tomato sauce and cheese"><span class="date">May 25, 2011</span></div>
      <div class="photo photo--b" role="img" aria-label="Photo of a stack of blueberry pancakes with cream and a strawberry"><span class="date">May 25, 2011</span></div>
      <div class="photo photo--c" role="img" aria-label="Photo of a pasta dish with vegetables"><span class="date">May 25, 2011</span></div>
    </div>
    <div class="ratings">
      <span>(5 ratings)</span>
      <span class="stars">
        <svg width="22" height="22" fill="var(--star)"><use href="#star"/></svg>
        <svg width="22" height="22" fill="var(--star)"><use href="#star"/></svg>
        <svg width="22" height="22" fill="var(--star)"><use href="#star"/></svg>
        <svg width="22" height="22" fill="var(--star-off)"><use href="#star"/></svg>
        <svg width="22" height="22" fill="var(--star-off)"><use href="#star"/></svg>
      </span>
    </div>
    <p class="desc">Lorem Ipsum proin gravida nibh vel velit auctor ali-quet. Aenean sollicitudin, lorem quis bibendum auctor, nisi elit consequat ipsum.</p>
    <div class="row row--price"><span>Student</span><span class="price">€3.90</span></div>
    <div class="row row--price"><span>Gast</span><span class="price">€4.90</span></div>
    <div class="row row--header"><span>Rating</span></div>
    <div class="rate-box">
      <svg width="38" height="38" fill="var(--star-off)"><use href="#star"/></svg>
      <svg width="38" height="38" fill="var(--star-off)"><use href="#star"/></svg>
      <svg width="38" height="38" fill="var(--star-off)"><use href="#star"/></svg>
      <svg width="38" height="38" fill="var(--star-off)"><use href="#star"/></svg>
      <svg width="38" height="38" fill="var(--star-off)"><use href="#star"/></svg>
    </div>
    <div class="row row--link"><span>2 Comment</span><svg width="14" height="18" viewBox="0 0 14 18"><path d="M3 2l7 7-7 7" fill="none" stroke="var(--text)" stroke-width="3"/></svg></div>
    <div class="row row--header last"><span>Additives</span></div>
  </section>

  <!-- Canteen list screen -->
  <section class="screen screen--list">
    <div class="status">
      <span class="signal"><i style="height:3px"></i><i style="height:5px"></i><i style="height:7px"></i><i style="height:9px"></i><i style="height:12px"></i></span>
      <span class="carrier">NIMBUS</span><span>3G</span>
      <svg class="lock" width="14" height="17" viewBox="0 0 14 17"><path d="M3 7V5a4 4 0 018 0v2" fill="none" stroke="#fff" stroke-width="2"/><rect x="1" y="7" width="12" height="10" rx="1" fill="#fff"/></svg>
      <svg class="battery" width="28" height="13" viewBox="0 0 28 13"><rect x="1" y="1" width="23" height="11" rx="2" fill="none" stroke="#fff" stroke-width="1.5"/><rect x="3" y="3" width="19" height="7" fill="#fff"/><rect x="25" y="4" width="2.5" height="5" fill="#fff"/></svg>
    </div>
    <header class="navbar">
      <span class="title">label</span>
      <div class="spacer"></div>
      <div class="nav-btn right"><svg width="40" height="40" viewBox="0 0 40 40"><circle cx="20" cy="20" r="18" fill="none" stroke="var(--icon)" stroke-width="2"/><path d="M12 19a8 8 0 0114-5m2 7a8 8 0 01-14 5" fill="none" stroke="var(--icon)" stroke-width="2.5"/><path d="M27 10v6h-6M13 30v-6h6" fill="none" stroke="var(--icon)" stroke-width="2.5"/></svg></div>
    </header>
    <ul style="list-style:none">
      <li class="venue"><h2>Baden-Wurttemberg</h2><p class="distance"><svg width="16" height="20" fill="var(--muted)"><use href="#pin"/></svg>Deistance : 185 km</p><p class="address">Lindenweg 12, 70199 Talheim</p><span class="fav"><svg width="34" height="34" fill="#3b434c"><use href="#heart"/></svg></span></li>
      <li class="venue"><h2>Baden-Wurttemberg</h2><p class="distance"><svg width="16" height="20" fill="var(--muted)"><use href="#pin"/></svg>Deistance : 185 km</p><p class="address">Lindenweg 12, 70199 Talheim</p><span class="fav"><svg width="34" height="34" fill="var(--accent)"><use href="#heart"/></svg></span></li>
      <li class="venue"><h2>Baden-Wurttemberg</h2><p class="distance"><svg width="16" height="20" fill="var(--muted)"><use href="#pin"/></svg>Deistance : 185 km</p><p class="address">Lindenweg 12, 70199 Talheim</p><span class="fav"><svg width="34" height="34" fill="#3b434c"><use href="#heart"/></svg></span></li>
      <li class="venue"><h2>Baden-Wurttemberg</h2><p class="distance"><svg width="16" height="20" fill="var(--muted)"><use href="#pin"/></svg>Deistance : 185 km</p><p class="address">Lindenweg 12, 70199 Talheim</p><span class="fav"><svg width="34" height="34" fill="var(--accent)"><use href="#heart"/></svg></span></li>
      <li class="venue"><h2>Baden-Wurttemberg</h2><p class="distance"><svg width="16" height="20" fill="var(--muted)"><use href="#pin"/></svg>Deistance : 185 km</p><p class="address">Lindenweg 12, 70199 Talheim</p><span class="fav"><svg width="34" height="34" fill="#3b434c"><use href="#heart"/></svg></span></li>
    </ul>
    <nav class="tabbar">
      <div class="tab"><svg width="32" height="30" viewBox="0 0 32 30"><path d="M3 3h26l2 7H1z" fill="var(--accent)"/><path d="M4 12h24v16H4z" fill="none" stroke="var(--accent)" stroke-width="3"/><path d="M10 18h12" stroke="var(--accent)" stroke-width="3"/></svg>Canteens</div>
      <div class="tab"><svg width="26" height="32" fill="#7f8892"><use href="#pin"/></svg>Map</div>
      <div class="tab"><svg width="34" height="32" fill="#7f8892"><use href="#heart"/></svg>Favorites</div>
    </nav>
  </section>
</div>
</body>
</html>
```